Personal Finance e-commerce website needs a simple budget design

Hello! I am starting to sell downloadable and printable budget planners, as shown in the attached file, for people to plan ahead on their personal finances. <br/><br/>I want to see a one-page design with similar columns (for example, "Expenses, Budget, and Actual"). I would also like to see the basic formula ("Net Income = Gross income - Total Expenses") somewhere on the design. Finally, I want the design to remain mostly minimalistic and simple for the average person to plan their personal monthly budgets.<br/><br/>However, other than that, the overall design, layout, and colors will be at the graphic designer's choice. If you have any questions for me, please let me know. Thank you for your time!

Industry/Entity Type

Financial Planning

Colors

Designer to choose colors to be used in the design.

Requirements
Must have
• I want to see a one-page design with similar columns (for example, "Expenses, Budget, and Actual").
• I want the design to remain mostly minimalistic and simple for the average person to plan their personal monthly budgets.
Nice to have
• I would also like to see the basic formula ("Net Income = Gross income - Total Expenses") somewhere on the design.

```html
<!DOCTYPE html>
<html lang="en">
<head>
<meta charset="utf-8">
<title>Basic Monthly Budget</title>
<link rel="stylesheet" href="https://fonts.googleapis.com/css2?family=Oswald:wght@400;500&family=Open+Sans:wght@400;600&display=swap">
<style>
  :root {
    --paper: #f3f4f4;
    --paper-edge: #e4e6e7;
    --ink: #111111;
    --muted: #7d7f82;
    --blue: #4a86c5;
    --blue-dark: #2f5f8c;
    --grey: #808185;
    --grey-dark: #58595c;
    --purple: #a8559f;
    --purple-dark: #5c3f7e;
    --purple-foot: #7a5aa0;
    --brand: #a8559f;
    --row-a: #c3ccd3;
    --row-b: #dde3e8;
    --row-mid-a: #dfe4e7;
    --row-mid-b: #eef1f2;
    --rule: #3d4350;
    --pill: #58595c;
    --white: #ffffff;
  }
  * { box-sizing: border-box; margin: 0; padding: 0; }
  html, body { width: 998px; height: 1200px; overflow: hidden; }
  body {
    background: radial-gradient(ellipse at 50% 45%, var(--paper) 55%, var(--paper-edge) 100%);
    font-family: "Open Sans", Arial, sans-serif;
    color: var(--ink);
    position: relative;
  }
  .visit {
    position: absolute; top: 44px; left: 262px;
    font-size: 16px; font-weight: 600;
  }
  .brand {
    position: absolute; left: 64px; top: 124px;
    font-family: "Oswald", sans-serif; font-weight: 500;
    font-size: 28px; line-height: 1;
    color: var(--brand);
    white-space: nowrap;
  }
  .title {
    position: absolute; left: 282px; top: 110px;
    font-family: "Oswald", sans-serif; font-weight: 500;
    font-size: 46px; letter-spacing: 0.5px; line-height: 1;
  }
  .period {
    position: absolute; left: 323px; top: 204px; width: 348px;
    border-top: 1px solid #b9bcbf;
    text-align: center; padding-top: 8px;
    font-family: "Oswald", sans-serif; font-size: 12px; color: var(--muted);
  }
  .budget-table {
    position: absolute; left: 65px; top: 292px;
    width: 880px; height: 684px;
    display: grid; grid-template-columns: repeat(3, 1fr);
  }
  .col { display: flex; flex-direction: column; }
  .col-head {
    height: 68px; border-radius: 20px 20px 0 0;
    display: flex; align-items: flex-end; justify-content: center;
    padding-bottom: 6px;
    font-family: "Oswald", sans-serif; font-weight: 500;
    font-size: 24px; color: var(--white);
  }
  .col-sub {
    height: 69px; padding-top: 10px; text-align: center;
    font-size: 15px; color: var(--white);
  }
  .col-sub.left { text-align: left; padding-left: 60px; }
  .col-rows {
    height: 486px;
    background: repeating-linear-gradient(to bottom,
      var(--row-a) 0 37.4px, var(--row-b) 37.4px 74.8px);
  }
  .col.mid .col-rows {
    background: repeating-linear-gradient(to bottom,
      var(--row-mid-a) 0 37.4px, var(--row-mid-b) 37.4px 74.8px);
    box-shadow: -4px 0 8px rgba(0,0,0,0.12), 4px 0 8px rgba(0,0,0,0.12);
    position: relative; z-index: 1;
  }
  .col-rule { height: 12px; background: var(--rule); }
  .col-foot { flex: 1; border-radius: 0 0 20px 20px; }
  .expenses .col-head, .expenses .col-foot { background: var(--blue); }
  .expenses .col-sub { background: var(--blue-dark); }
  .mid .col-head, .mid .col-foot { background: var(--grey); }
  .mid .col-sub { background: var(--grey-dark); }
  .actual .col-head { background: var(--purple); }
  .actual .col-sub { background: var(--purple-dark); }
  .actual .col-foot { background: var(--purple-foot); }

  .formula { position: absolute; top: 1024px; left: 0; width: 998px; height: 90px; }
  .term { position: absolute; top: 0; width: 258px; }
  .term-tag {
    height: 48px; margin-top: 10px;
    clip-path: polygon(0 0, 94% 0, 100% 50%, 94% 100%, 0 100%);
    display: flex; align-items: center; justify-content: center; padding-right: 14px;
    font-family: "Oswald", sans-serif; font-weight: 500; font-size: 24px; color: var(--white);
  }
  .term::before {
    content: ""; position: absolute; left: 0; top: 0;
    border-bottom: 10px solid #5b6470; border-left: 10px solid transparent;
  }
  .term-note { text-align: center; font-size: 13px; color: var(--muted); margin-top: 14px; padding-right: 14px; }
  .term.net { left: 57px; } .term.net .term-tag { background: var(--blue); }
  .term.gross { left: 372px; } .term.gross .term-tag { background: var(--blue); }
  .term.total { left: 680px; } .term.total .term-tag { background: var(--purple); }
  .operator {
    position: absolute; top: 20px; line-height: 1;
    font-family: "Oswald", sans-serif; font-weight: 500; font-size: 46px;
  }
  .operator.eq { left: 330px; } .operator.minus { left: 648px; }

  .site-pill {
    position: absolute; left: 289px; top: 1139px; width: 418px; height: 40px;
    border-radius: 20px; background: var(--pill);
    box-shadow: 0 4px 6px rgba(0,0,0,0.25);
    display: flex; align-items: center; justify-content: center; gap: 10px;
    color: var(--white); font-size: 22px; letter-spacing: 1px;
  }
</style>
</head>
<body>
  <p class="visit">Visit us at: claravennet.com &nbsp;for personal financial advice!</p>
  <div class="brand">Clara Vennet</div>
  <h1 class="title">BASIC MONTHLY BUDGET</h1>
  <div class="period">MONTH / YEAR</div>

  <section class="budget-table">
    <div class="col expenses">
      <div class="col-head">EXPENSES (CATEGORY)</div>
      <div class="col-sub left">Custom category</div>
      <div class="col-rows"></div>
      <div class="col-rule"></div>
      <div class="col-foot"></div>
    </div>
    <div class="col mid">
      <div class="col-head">BUDGER (USD)</div>
      <div class="col-sub">What you plan to spend</div>
      <div class="col-rows"></div>
      <div class="col-rule"></div>
      <div class="col-foot"></div>
    </div>
    <div class="col actual">
      <div class="col-head">ACTUAL (USD)</div>
      <div class="col-sub">What you actully spent</div>
      <div class="col-rows"></div>
      <div class="col-rule"></div>
      <div class="col-foot"></div>
    </div>
  </section>

  <section class="formula">
    <div class="term net"><div class="term-tag">NET INCOME</div><p class="term-note">how much money you kept</p></div>
    <span class="operator eq">=</span>
    <div class="term gross"><div class="term-tag">GROSS INCOME</div><p class="term-note">how much money you earned</p></div>
    <span class="operator minus">-</span>
    <div class="term total"><div class="term-tag">TOTAL EXPENSES</div><p class="term-note">actual expenses</p></div>
  </section>

  <div class="site-pill">
    <svg width="20" height="20" viewBox="0 0 20 20" fill="none" stroke="#ffffff" stroke-width="1.6" aria-hidden="true">
      <circle cx="10" cy="10" r="8.2"/>
      <ellipse cx="10" cy="10" rx="3.6" ry="8.2"/>
      <line x1="1.8" y1="10" x2="18.2" y2="10"/>
      <line x1="3.2" y1="5.6" x2="16.8" y2="5.6"/>
      <line x1="3.2" y1="14.4" x2="16.8" y2="14.4"/>
    </svg>
    <span>www.claravennet.com</span>
  </div>
</body>
</html>
```